Consultancy Business Card Design

We need a business card design for a new company based in singapore called FortyOne. FortyOne a boutique consultancy firm offering broad-based business solutions, from conception to re-invention, for ventures from new start-ups to long-running traditional businesses.
Its 2 main divisions (Food & Beverage Operations and Construction & Project Management) have access to a wide range of networks, knowledge bases, and resources to service its clients across numerous diverse sectors. This includes, and is not limited to, construction, F&B, and retail.
We are a company that combines the ambition, boldness and energy of one in the 20s with the dedication, level-headedness and dependability of one entering its 30s. Bridging the experiences of the old with ideals of the young, we draw on the positives of both to create a unique synergy.
We hope to see designs that fits our company profile.
Boutique
FortyOne(Company Name)
Marcus Leow (Name)
Principle Consultant (Title)
F&B and Hospitality (Division)
(+65) 8364 5170 (Contact no.)
marcus@fortyone-example.com.sg (Email)

```html
<!DOCTYPE html>
<html lang="en">
<head>
<meta charset="utf-8">
<title>FortyOne Business Card</title>
<link rel="stylesheet" href="https://fonts.googleapis.com/css2?family=Exo+2:wght@400;500&display=swap">
<style>
  :root {
    --page: #e4e6e8;
    --card-black: #141414;
    --card-black-soft: #2a2a2a;
    --brand-blue: #2b8fd0;
    --blue-light: #cfe6f5;
    --white: #ffffff;
    --title-yellow: #e8e21c;
    --division-green: #7cc242;
    --icon-blue: #6cc3ee;
  }
  * { margin: 0; padding: 0; box-sizing: border-box; }
  html, body {
    width: 1200px; height: 1200px; overflow: hidden;
    background: var(--page);
    font-family: "Exo 2", sans-serif;
  }
  .canvas {
    position: relative; width: 1200px; height: 1200px;
  }
  .card {
    position: absolute; left: 150px; width: 900px; height: 514px;
    overflow: hidden; border-radius: 4px;
    box-shadow: 0 6px 18px rgba(0,0,0,0.25);
  }
  .card--front { top: 50px; background: radial-gradient(ellipse at 50% 40%, var(--card-black-soft), var(--card-black) 75%); }
  .card--back { top: 630px; }
  .card__art { position: absolute; inset: 0; width: 100%; height: 100%; }

  .brand {
    position: absolute; display: flex; align-items: center; gap: 16px;
    color: var(--white); font-weight: 500; letter-spacing: 2px;
  }
  .brand__square { width: 0.7em; height: 0.7em; background: var(--brand-blue); }
  .card--front .brand { left: 50%; top: 50%; transform: translate(-50%, -50%); font-size: 92px; }
  .card--back .brand { right: 56px; top: 92px; font-size: 60px; gap: 12px; }

  .contact { position: absolute; left: 40px; top: 232px; }
  .contact__name { color: var(--white); font-size: 42px; font-weight: 500; letter-spacing: 1px; line-height: 1.1; }
  .contact__title { color: var(--title-yellow); font-size: 26px; line-height: 1.2; margin-top: 4px; }
  .contact__division { color: var(--division-green); font-size: 26px; line-height: 1.2; }
  .contact__rule { width: 430px; height: 2px; background: var(--white); margin: 14px 0 18px; }
  .contact__row { display: flex; align-items: center; gap: 14px; color: var(--white); font-size: 30px; line-height: 1.5; letter-spacing: 1px; }
  .contact__icon { width: 28px; height: 24px; flex: none; }
</style>
</head>
<body>
<main class="canvas">
  <section class="card card--front" aria-label="Card front">
    <div class="brand"><span class="brand__square"></span><span class="brand__name">FortyOne</span></div>
  </section>

  <section class="card card--back" aria-label="Card back">
    <svg class="card__art" viewBox="0 0 900 514" preserveAspectRatio="none" aria-hidden="true">
      <defs>
        <linearGradient id="blueCornerTop" x1="0" y1="0" x2="1" y2="1">
          <stop offset="0" stop-color="var(--blue-light)"/>
          <stop offset="0.6" stop-color="var(--brand-blue)"/>
        </linearGradient>
        <linearGradient id="blueCornerBottom" x1="0" y1="0" x2="1" y2="1">
          <stop offset="0.4" stop-color="var(--brand-blue)"/>
          <stop offset="1" stop-color="var(--blue-light)"/>
        </linearGradient>
        <radialGradient id="blackPanel" cx="0.55" cy="0.45" r="0.7">
          <stop offset="0" stop-color="#2c2c2c"/>
          <stop offset="1" stop-color="#0f0f0f"/>
        </radialGradient>
      </defs>
      <rect width="450" height="514" fill="url(#blueCornerTop)"/>
      <rect x="450" width="450" height="514" fill="url(#blueCornerBottom)"/>
      <path d="M0,190 Q130,30 470,0 L900,0 L900,270 Q820,470 430,514 L0,514 Z" fill="url(#blackPanel)"/>
    </svg>

    <div class="brand"><span class="brand__square"></span><span class="brand__name">FortyOne</span></div>

    <div class="contact">
      <p class="contact__name">Marcus Leow</p>
      <p class="contact__title">Principle Consultant</p>
      <p class="contact__division">F&amp;B and Hospitality (Division)</p>
      <div class="contact__rule"></div>
      <p class="contact__row">
        <svg class="contact__icon" viewBox="0 0 28 24" aria-hidden="true">
          <path d="M2,8 Q14,-2 26,8 L22,11 L19,7 Q14,5 9,7 L6,11 Z" fill="var(--icon-blue)"/>
          <path d="M7,12 L10,9 L18,9 L21,12 L23,22 L5,22 Z" fill="var(--icon-blue)"/>
          <circle cx="14" cy="16" r="3" fill="var(--card-black)"/>
        </svg>
        <span>(+65) 8364 5170</span>
      </p>
      <p class="contact__row">
        <svg class="contact__icon" viewBox="0 0 28 24" aria-hidden="true">
          <rect x="1" y="3" width="26" height="18" fill="var(--icon-blue)"/>
          <path d="M1,3 L14,14 L27,3" fill="none" stroke="var(--card-black)" stroke-width="2"/>
        </svg>
        <span>marcus@fortyone-example.com.sg</span>
      </p>
    </div>
  </section>
</main>
</body>
</html>
```